Thornwell Building Company - advertisement poster

I am looking to print some canvas signs to advertise my general contracting company, Thornwell Building Company. The sign will measure 6' long x 3' high so the size should match that ratio. I already have a logo icon, which is the Letter 'T' and some trees that I would like to incorporate, see attached. I would also like the to have the following information listed:
1) phone number: 472-555-0188
2) email: thornwellbuildingcompany@mailvero.com
3) website: thornwellbuildingcompany.com
4) Lic#4620385
5) I want to use this text: "BUILD WITH THE T-CREW!"

The ad should be relatively simple and clean. Black and Green are my company colors. I am open to creative ideas!

Target Market(s)

People looking to renovate their homes

Industry/Entity Type

Construction

Colors
59FF00
82FF00
B8FF75
E3FFCB
F4FFEA

Requirements
Must have
• Must have my company logo
Should not have
• No photos or complex graphics

```html
<!DOCTYPE html>
<html lang="en">
<head>
<meta charset="utf-8">
<title>Thornwell Building Company – Build with the T-Crew</title>
<link rel="stylesheet" href="https://fonts.googleapis.com/css2?family=Orbitron:wght@500;700;900&family=Questrial&display=swap">
<style>
  :root {
    --black: #000000;
    --charcoal: #1a1a1a;
    --green: #6db145;
    --green-mid: #5c8d3e;
    --green-dark: #486633;
    --white: #ffffff;
  }
  html, body {
    margin: 0;
    padding: 0;
    width: 1200px;
    height: 800px;
    overflow: hidden;
    background: var(--black);
  }
  .poster { display: block; width: 1200px; height: 800px; }
  .bg-right { fill: var(--black); }
  .bg-left { fill: var(--charcoal); }
  .band-light { fill: var(--green); }
  .band-mid { fill: var(--green-mid); }
  .band-dark { fill: var(--green-dark); }
  .bolt-line { fill: none; stroke: var(--green); stroke-width: 9; stroke-linejoin: miter; }
  .headline { font-family: "Orbitron", sans-serif; font-weight: 900; fill: var(--white); font-size: 90px; }
  .crew-pill-outer { fill: var(--green); }
  .crew-pill-inner { fill: var(--black); }
  .crew-text { font-family: "Orbitron", sans-serif; font-weight: 900; fill: var(--green); font-size: 84px; }
  .phone { font-family: "Orbitron", sans-serif; font-weight: 700; fill: var(--white); font-size: 48px; }
  .contact { font-family: "Questrial", sans-serif; fill: var(--green); font-size: 18px; }
  .contact-icon { fill: none; stroke: var(--green); stroke-width: 1.6; }
  .logo-mark { fill: var(--green); }
  .company-name { font-family: "Orbitron", sans-serif; font-weight: 900; fill: var(--white); font-size: 74px; }
  .company-sub { font-family: "Orbitron", sans-serif; font-weight: 500; fill: var(--green); font-size: 27px; }
  .license { font-family: "Orbitron", sans-serif; font-weight: 500; fill: var(--green); font-size: 27px; }
</style>
</head>
<body>
<svg class="poster" viewBox="0 0 1200 800" xmlns="http://www.w3.org/2000/svg" role="img" aria-label="Build with the T-Crew – Thornwell Building Company">
  <!-- background split -->
  <rect class="bg-right" x="0" y="0" width="1200" height="800"/>
  <polygon class="bg-left" points="0,0 762,0 516,333 651,333 444,597 591,597 429,800 0,800"/>

  <!-- diagonal accent bands -->
  <polygon class="band-dark" points="0,0 468,0 0,624"/>
  <polygon class="band-mid" points="0,0 408,0 0,544"/>
  <polygon class="band-light" points="0,0 360,0 0,480"/>

  <!-- zigzag divider -->
  <polyline class="bolt-line" points="762,-5 516,329 651,329 444,593 591,593 426,805"/>

  <!-- headline -->
  <text class="headline" x="51" y="126" textLength="351" lengthAdjust="spacingAndGlyphs">BUILD</text>
  <text class="headline" x="51" y="224" textLength="303" lengthAdjust="spacingAndGlyphs">WITH</text>
  <text class="headline" x="51" y="320" textLength="234" lengthAdjust="spacingAndGlyphs">THE</text>

  <!-- T-Crew pill -->
  <rect class="crew-pill-outer" x="17" y="363" width="505" height="127" rx="52"/>
  <rect class="crew-pill-inner" x="25" y="371" width="489" height="111" rx="45"/>
  <text class="crew-text" x="51" y="456" textLength="435" lengthAdjust="spacingAndGlyphs">T-CREW</text>

  <!-- contact -->
  <text class="phone" x="33" y="666" textLength="471" lengthAdjust="spacingAndGlyphs">472-555-0188</text>

  <g class="contact-icon" transform="translate(33,701)">
    <rect x="0" y="0" width="17" height="12" rx="2"/>
    <polyline points="1,1.5 8.5,7 16,1.5"/>
  </g>
  <text class="contact" x="64" y="713" textLength="404" lengthAdjust="spacing">thornwellbuildingcompany@mailvero.com</text>

  <g class="contact-icon" transform="translate(42,735)">
    <circle cx="0" cy="0" r="8"/>
    <ellipse cx="0" cy="0" rx="3.5" ry="8"/>
    <line x1="-8" y1="0" x2="8" y2="0"/>
    <line x1="-7" y1="-4" x2="7" y2="-4"/>
    <line x1="-7" y1="4" x2="7" y2="4"/>
  </g>
  <text class="contact" x="64" y="741" textLength="328" lengthAdjust="spacing">thornwellbuildingcompany.com</text>

  <!-- company logo placeholder -->
  <rect class="logo-mark" x="743" y="195" width="300" height="300" role="img" aria-label="Thornwell Building Company logo"/>

  <!-- company name -->
  <text class="company-name" x="617" y="571" textLength="551" lengthAdjust="spacingAndGlyphs">THORNWELL</text>
  <text class="company-sub" x="619" y="607" textLength="549" lengthAdjust="spacing">BUILDING COMPANY</text>

  <!-- license -->
  <text class="license" x="708" y="723" textLength="369" lengthAdjust="spacing">LICENSE# 4620385</text>
</svg>
</body>
</html>
```